Generic Business Card

We are a high end podiatry clinic in Cottesloe, Western Australia looking to connect with like-minded health care professionals. We want to convey our expertise in biomechanical conditions and treatment in particular. The business card should be modern, professional, and minimal in design. The business card should give a bright, energetic, friendly, and inviting impression. We would like to include our company colours of orange and deep blue as well as a QR code that will direct people to our book online page (see attached image). We would also like to include general information like our phone number and address. We do not want to include specific names on this business card. We have included an example with our company details.

```html
<!DOCTYPE html>
<html lang="en">
<head>
<meta charset="utf-8">
<title>The Stride Clinic – Business Card</title>
<link href="https://fonts.googleapis.com/css2?family=Lexend:wght@300;400&display=swap" rel="stylesheet">
<style>
  :root{
    --canvas:#ebebeb;
    --navy:#233d80;
    --navy-deep:#1f3674;
    --navy-ink:#3a4670;
    --orange:#f2722b;
    --white:#ffffff;
  }
  *{box-sizing:border-box;margin:0;padding:0}
  html,body{width:1200px;height:1200px;overflow:hidden}
  body{background:var(--canvas);position:relative;font-family:"Lexend",sans-serif;font-weight:300}
  .card{position:absolute;left:156px;width:888px;height:519px;background:var(--white);overflow:hidden}
  .card--front{top:72px}
  .card--back{top:619px}
  .card__art{position:absolute;inset:0;width:100%;height:100%}
  .contact{position:absolute;left:60px;top:142px;list-style:none;color:var(--white);font-size:23px;line-height:34px}
  .contact__item{display:flex;align-items:flex-start;gap:20px}
  .contact__icon{width:18px;height:18px;margin-top:8px;flex:none}
  .contact__text{display:block}
  .tagline{position:absolute;left:60px;top:360px;color:var(--white);font-size:23px;line-height:34px}
  .brand-front{position:absolute;left:601px;width:240px;top:160px;text-align:center}
  .brand-front__mark{display:block;margin:0 auto;width:120px;height:120px;border:2.5px solid var(--orange);border-radius:50%}
  .brand-front__name{display:block;margin-top:26px;font-size:30px;font-weight:400;color:var(--navy);white-space:nowrap}
  .brand-back{position:absolute;left:0;right:0;top:120px;text-align:center}
  .brand-back__mark{display:block;margin:0 auto;width:214px;height:214px;border:3px solid var(--navy-ink);border-radius:50%}
  .brand-back__name{display:block;margin-top:12px;font-size:54px;font-weight:400;color:var(--orange);white-space:nowrap}
</style>
</head>
<body>
  <section class="card card--front" aria-label="Business card front">
    <svg class="card__art" viewBox="0 0 888 519" aria-hidden="true">
      <defs>
        <linearGradient id="navyField" x1="0" y1="0" x2="1" y2="1">
          <stop offset="0" stop-color="#26418a"/>
          <stop offset="1" stop-color="#1f3674"/>
        </linearGradient>
      </defs>
      <path d="M0 0 H636 C515 140 505 370 655 519 H0 Z" fill="url(#navyField)"/>
      <path d="M650 0 H706 C580 120 555 360 668 519 H661 C524 380 538 130 650 0 Z" fill="var(--orange)"/>
    </svg>

    <ul class="contact">
      <li class="contact__item">
        <svg class="contact__icon" viewBox="0 0 18 18" aria-hidden="true"><rect x="5" y="1.5" width="8" height="15" rx="1.5" fill="none" stroke="#fff" stroke-width="1.5"/><line x1="8" y1="14" x2="10" y2="14" stroke="#fff" stroke-width="1.5"/></svg>
        <span class="contact__text">08 9000 4812</span>
      </li>
      <li class="contact__item">
        <svg class="contact__icon" viewBox="0 0 18 18" aria-hidden="true"><circle cx="9" cy="9" r="7.2" fill="none" stroke="#fff" stroke-width="1.4"/><ellipse cx="9" cy="9" rx="3.2" ry="7.2" fill="none" stroke="#fff" stroke-width="1.2"/><line x1="1.8" y1="9" x2="16.2" y2="9" stroke="#fff" stroke-width="1.2"/></svg>
        <span class="contact__text">www.thestrideclinic.net</span>
      </li>
      <li class="contact__item">
        <svg class="contact__icon" viewBox="0 0 18 18" aria-hidden="true"><path d="M9 1.5a4.5 4.5 0 0 0-4.5 4.5c0 3.3 4.5 7.5 4.5 7.5s4.5-4.2 4.5-7.5A4.5 4.5 0 0 0 9 1.5z" fill="none" stroke="#fff" stroke-width="1.4"/><circle cx="9" cy="6" r="1.6" fill="#fff"/><line x1="3" y1="16.5" x2="15" y2="16.5" stroke="#fff" stroke-width="1.4"/></svg>
        <span class="contact__text">Seabreeze Plaza,<br>212 Marine Parade, Westshore</span>
      </li>
    </ul>

    <p class="tagline">Steady Your Steps,<br>Build on Firm Footing</p>

    <div class="brand-front">
      <span class="brand-front__mark" aria-hidden="true"></span>
      <span class="brand-front__name">The Stride Clinic</span>
    </div>
  </section>

  <section class="card card--back" aria-label="Business card back">
    <div class="brand-back">
      <span class="brand-back__mark" aria-hidden="true"></span>
      <span class="brand-back__name">The Stride Clinic</span>
    </div>
  </section>
</body>
</html>
```